Web Design for integrated onestop building services provider of Mechanical and Electrical (M&E) eng

Web Design for a Singapore-based integrated one-stop building services provider of Mechanical and Electrical (M&E) engineering services for the building and construction industry.

Background colour: white
Scheme Colour: white, green, some grey (Please refer to logo)

Final File Output for 5 Pages
(Home Page, General Content Page, Who We Are, Accreditations & Awards, Career Page)

- Responsive with Parallax effects, BOOTSTRAP3 Standard Coding

- Stock Images for Banner Slider/Background
(Mechanical and Electrical (M&E) engineering services for the building and construction industry.

Please see attachment for more details.
Updates

Project Deadline Extended
Reason: Please submit some initial design up by 19th Aug for some feedbacks.

Target Market(s)

Singapore, Asia & International

Industry/Entity Type

Engineering

Coding

Coded - Design and coding required

Number of Pages Required

5+ page

Font styles to use
Sans Serif

Colors
ffffff
00a990
edf8f6

Requirements
Must have
• Boostrap 3.0, parallex, please follow requirements
• modern, technology, engineering look
Nice to have
• Stock Photos
Should not have
• TBA

```html
<!DOCTYPE html>
<html lang="en">
<head>
<meta charset="utf-8">
<title>Arcline Engineering Pte Ltd</title>
<link href="https://fonts.googleapis.com/css2?family=Open+Sans:wght@400;600;700&family=Roboto+Condensed:wght@400;700&display=swap" rel="stylesheet">
<style>
:root{
  --green:#00a990;
  --green-dark:#008a75;
  --mint:#edf8f6;
  --white:#ffffff;
  --ink:#333a3f;
  --grey:#7b8288;
  --grey-light:#d9dcde;
  --footer:#2b2e31;
  --footer-bar:#1f2124;
}
*{box-sizing:border-box;margin:0;padding:0}
html,body{width:1200px;height:2284px;overflow:hidden;background:var(--white)}
body{font-family:"Open Sans",Arial,sans-serif;color:var(--ink);position:relative}
.heading{font-family:"Roboto Condensed","Arial Narrow",sans-serif;font-weight:700;text-transform:uppercase}

/* header */
.site-header{position:absolute;top:0;left:0;width:1200px;height:72px;display:flex;align-items:center;justify-content:space-between;padding:0 40px;background:var(--white);border-bottom:1px solid var(--grey-light)}
.brand{display:flex;align-items:center;gap:10px;font-family:"Open Sans",sans-serif;font-weight:700;font-size:17px;color:var(--green)}
.brand-dot{width:34px;height:34px;border-radius:50%;background:var(--green)}
.main-nav{display:flex;gap:22px;align-items:center;font-size:13px;font-weight:600}
.main-nav a{color:var(--ink);text-decoration:none}
.main-nav a.active{color:var(--green)}

/* hero */
.hero{position:absolute;top:72px;left:0;width:1200px;height:448px;background:linear-gradient(180deg,#27527e 0%,#3c6f9a 45%,#b27a3b 78%,#2a2a33 100%);text-align:center;color:var(--white)}
.hero-title{margin-top:140px;font-family:"Open Sans",sans-serif;font-weight:700;font-size:48px}
.hero-text{width:560px;margin:14px auto 0;font-size:15px;line-height:1.5}
.btn-outline{display:inline-block;margin-top:24px;padding:9px 24px;border:2px solid var(--white);font-size:13px;font-weight:700;letter-spacing:1px;color:var(--white)}
.hero-arrow{position:absolute;top:200px;width:30px;height:40px}
.hero-arrow.prev{left:30px}.hero-arrow.next{right:30px}

/* intro */
.intro-card{position:absolute;top:560px;height:200px;padding:30px 36px}
.intro-card.who{left:0;width:592px;background:var(--green);color:var(--white)}
.intro-card.what{left:604px;width:588px;background:var(--mint);border:2px solid var(--grey-light)}
.intro-card h2{font-size:28px;display:flex;align-items:center;gap:10px}
.intro-card.what h2{color:var(--ink)}
.intro-card p{margin-top:14px;font-size:13px;line-height:1.6;width:440px}
.intro-card ul{margin-top:14px;font-size:13px;line-height:1.8;list-style:none;color:var(--grey)}
.intro-card li::before{content:"•";color:var(--green);margin-right:8px}
.btn-small{display:inline-block;margin-top:16px;padding:5px 14px;font-size:11px;font-weight:700;border:1px solid currentColor}
.intro-card.what .btn-small{color:var(--green)}

/* accomplishments */
.accomplished{position:absolute;top:790px;left:0;width:1200px;height:360px;text-align:center}
.accomplished h2{font-size:32px;color:var(--ink)}
.accomplished .sub{margin-top:6px;font-size:15px;font-style:italic;color:var(--green)}
.stats{position:absolute;top:0;left:0}
.stat-label{position:absolute;top:290px;width:300px;font-size:15px;color:var(--ink)}
.counter-box{position:absolute;top:152px;left:530px;width:140px;height:36px;border:2px solid var(--grey-light);background:var(--white);font-size:12px;font-weight:700;line-height:32px}

/* accreditations */
.accreditations{position:absolute;top:1160px;left:0;width:1200px;height:340px;background:linear-gradient(180deg,#4a4d50,#2f3134)}
.accreditations h2{margin-top:40px;text-align:center;font-size:34px;color:var(--white)}
.badge{position:absolute;background:var(--white);border-radius:4px}

/* projects */
.projects{position:absolute;top:1520px;left:0;width:1200px;height:480px;text-align:center}
.projects h2{font-size:34px;color:var(--ink)}
.world-map{position:absolute;top:70px;left:200px;width:800px;height:390px;background:radial-gradient(ellipse at center,#e6e8ea 0%,#f3f4f5 70%,#ffffff 100%);border-radius:40px}

/* footer */
.site-footer{position:absolute;top:2020px;left:0;width:1200px;height:220px;background:var(--footer);border-top:5px solid var(--green);color:#c8cbcd;padding:30px 40px;display:flex}
.site-footer h3{font-size:15px;color:var(--white);margin-bottom:18px}
.footer-col.social{width:340px}
.footer-col.career{width:440px}
.footer-col.office{flex:1}
.social-links{display:flex;gap:22px;font-size:13px}
.social-links span{display:flex;align-items:center;gap:8px}
.sq{width:14px;height:14px;background:#8a8f93}
.career-lists{display:flex;gap:26px}
.career-lists ul{list-style:none;font-size:11px;line-height:1.9}
.office p{font-size:12px;line-height:1.5;margin-bottom:8px;display:flex;gap:10px}
.office svg{flex:none;margin-top:2px}
.footer-bar{position:absolute;top:2240px;left:0;width:1200px;height:44px;background:var(--footer-bar);color:#9a9ea2;font-size:11px;text-align:center;line-height:44px}
</style>
</head>
<body>

<header class="site-header">
  <div class="brand"><span class="brand-dot"></span>Arcline Engineering Pte Ltd</div>
  <nav class="main-nav">
    <a class="active">Home</a><a>Who We Are</a><a>What We Do</a><a>Our Accomplishments</a><a>Accreditations &amp; Awards</a><a>Career</a><a>Contact Us</a>
    <svg width="14" height="14" viewBox="0 0 14 14"><circle cx="6" cy="6" r="4.5" fill="none" stroke="#333a3f" stroke-width="2"/><line x1="9.5" y1="9.5" x2="13" y2="13" stroke="#333a3f" stroke-width="2"/></svg>
  </nav>
</header>

<section class="hero" role="img" aria-label="Industrial power plant lit up at dusk">
  <h1 class="hero-title">Arcline Engineering Pte Ltd</h1>
  <p class="hero-text">Singapore-based integrated one-stop building services provider of Mechanical and Electrical (M&amp;E) engineering services for the building and construction industry.</p>
  <span class="btn-outline">GET MORE INFO &rarr;</span>
  <svg class="hero-arrow prev" viewBox="0 0 30 40"><polyline points="22,6 8,20 22,34" fill="none" stroke="#fff" stroke-width="4"/></svg>
  <svg class="hero-arrow next" viewBox="0 0 30 40"><polyline points="8,6 22,20 8,34" fill="none" stroke="#fff" stroke-width="4"/></svg>
</section>

<section class="intro-card who">
  <h2 class="heading"><svg width="24" height="24" viewBox="0 0 24 24"><circle cx="12" cy="12" r="11" fill="#fff"/><rect x="10.5" y="10" width="3" height="8" fill="#00a990"/><circle cx="12" cy="6.5" r="1.8" fill="#00a990"/></svg>Who We Are</h2>
  <p>Established in 1974, Arcline Engineering Pte. Ltd. is a Singapore-based integrated one-stop building services provider of Mechanical and Electrical (M&amp;E) engineering services for the building and construction industry.</p>
  <span class="btn-small">READ MORE &rarr;</span>
</section>

<section class="intro-card what">
  <h2 class="heading"><svg width="24" height="24" viewBox="0 0 24 24"><circle cx="9" cy="10" r="6" fill="none" stroke="#00a990" stroke-width="3"/><circle cx="18" cy="17" r="4" fill="none" stroke="#00a990" stroke-width="2.5"/></svg>What We Do</h2>
  <ul>
    <li>Whole system approach in design &amp; build</li>
    <li>Complete production &amp; maintenance works</li>
    <li>Trusted partner in customer project development</li>
  </ul>
  <span class="btn-small">READ MORE &rarr;</span>
</section>

<section class="accomplished">
  <h2 class="heading">What We Accomplished</h2>
  <p class="sub">Key Construction Projects Completed</p>
  <svg class="stats" width="1200" height="360" viewBox="0 0 1200 360">
    <line x1="355" y1="170" x2="845" y2="170" stroke="#c9cdd0" stroke-width="14"/>
    <polygon points="352,150 330,170 352,190" fill="#c9cdd0"/>
    <polygon points="848,150 870,170 848,190" fill="#c9cdd0"/>
    <circle cx="252" cy="170" r="100" fill="#fff" stroke="#e3e6e8" stroke-width="8"/>
    <circle cx="252" cy="170" r="100" fill="none" stroke="#00a990" stroke-width="8" stroke-dasharray="402 628" transform="rotate(-90 252 170)"/>
    <circle cx="948" cy="170" r="100" fill="#fff" stroke="#e3e6e8" stroke-width="8"/>
    <circle cx="948" cy="170" r="100" fill="none" stroke="#00a990" stroke-width="8" stroke-dasharray="320 628" transform="rotate(-90 948 170)"/>
    <text x="252" y="186" text-anchor="middle" font-family="Open Sans, sans-serif" font-size="46" fill="#333a3f">64%</text>
    <text x="948" y="186" text-anchor="middle" font-family="Open Sans, sans-serif" font-size="46" fill="#333a3f">51%</text>
  </svg>
  <div class="counter-box">LIVE COUNTER ?</div>
  <p class="stat-label" style="left:102px">No of Projects Completed</p>
  <p class="stat-label" style="left:798px">No of Projects Ongoing</p>
</section>

<section class="accreditations" role="img" aria-label="Engineering plant room with machinery">
  <h2 class="heading">Accreditations &amp; Awards</h2>
  <div class="badge" style="left:240px;top:150px;width:220px;height:110px"></div>
  <div class="badge" style="left:530px;top:150px;width:200px;height:110px"></div>
  <div class="badge" style="left:820px;top:140px;width:90px;height:130px"></div>
</section>

<section class="projects">
  <h2 class="heading">Come See Our Ongoing Projects!</h2>
  <div class="world-map" role="img" aria-label="World map marking ongoing project locations"></div>
</section>

<footer class="site-footer">
  <div class="footer-col social">
    <h3>SOCIAL MEDIA</h3>
    <div class="social-links"><span><i class="sq"></i>Linkbook</span><span><i class="sq"></i>Snapgram</span></div>
  </div>
  <div class="footer-col career">
    <h3>CAREER</h3>
    <div class="career-lists">
      <ul><li>› Engineering</li><li>› Facilities</li><li>› Consulting</li><li>› Site Services</li><li>› Procurement</li></ul>
      <ul><li>› Engineering</li><li>› Facilities</li><li>› Consulting</li><li>› Site Services</li><li>› Procurement</li></ul>
      <ul><li>› Engineering</li><li>› Facilities</li><li>› Consulting</li><li>› Site Services</li><li>› Procurement</li></ul>
    </div>
  </div>
  <div class="footer-col office">
    <h3>HQ OFFICE</h3>
    <p><svg width="10" height="14" viewBox="0 0 10 14"><path d="M5 0a5 5 0 0 1 5 5c0 4-5 9-5 9S0 9 0 5a5 5 0 0 1 5-5z" fill="#00a990"/></svg>18 Kallang Crescent #04-12,<br>Singapore 339420</p>
    <p><svg width="12" height="12" viewBox="0 0 12 12"><path d="M2 0l3 3-1.5 1.5a7 7 0 0 0 4 4L9 7l3 3-2 2C5 12 0 7 0 2z" fill="#00a990"/></svg>+65 6123 4501</p>
    <p><svg width="12" height="12" viewBox="0 0 12 12"><path d="M2 0l3 3-1.5 1.5a7 7 0 0 0 4 4L9 7l3 3-2 2C5 12 0 7 0 2z" fill="#00a990"/></svg>+65 6123 4502</p>
    <p><svg width="12" height="10" viewBox="0 0 12 10"><rect width="12" height="10" fill="#00a990"/><polyline points="0,0 6,5 12,0" fill="none" stroke="#2b2e31"/></svg>info@arclineeng.example</p>
  </div>
</footer>
<div class="footer-bar">Copyright © 2016, Arcline Engineering Pte Ltd. All rights reserved. Site Map | Disclaimer</div>

</body>
</html>
```